Political themed graphic for contemporary church sermon series

Contemporary church in California need a graphic design for a sermon series. The sermon series will be focused on the upcoming presidential election. The sermon series is titled for the question "who will be the next president":

Title: 45
Subtitle: Who will it be / Does it matter

The design should use red, white and blue and should possibly have the amber lodge in the graphic somewhere. Maybe like a watermark or something to that effect.

Target Market(s)

Contemporary design,

Industry/Entity Type

Church

Font styles to use
Serif
Sans Serif

Colors
0555a3
ec1f27
ffffff

Requirements
Must have
• Political theme, red, white and blue (contemporary color palette). Amber lodge screened back in the design somewhere.
• the title large: 45
• and subtitle: Who will it be | Does it matter
Should not have
• I'm not looking for cheesy graphics with elephant and a donkey.

```html
<!DOCTYPE html>
<html lang="en">
<head>
<meta charset="utf-8">
<title>45 — Sermon Series</title>
<link rel="stylesheet" href="https://fonts.googleapis.com/css2?family=Anton&family=Montserrat:wght@800&display=swap">
<style>
  :root {
    --flag-blue: #0555a3;
    --flag-red: #ec1f27;
    --paper: #ffffff;
    --mist: #ebebeb;
    --divider: #2b2b2b;
  }
  html, body {
    margin: 0;
    padding: 0;
    width: 1200px;
    height: 700px;
    overflow: hidden;
  }
  .series-graphic {
    position: relative;
    width: 1200px;
    height: 700px;
    overflow: hidden;
    background:
      linear-gradient(180deg, rgba(225,225,225,0.55) 0%, rgba(255,255,255,0) 55%),
      linear-gradient(90deg,
        var(--flag-blue) 0%,
        #7fa2c9 14%,
        #e3e8ee 32%,
        var(--mist) 50%,
        #f3e4e4 66%,
        #f0a5a7 84%,
        var(--flag-red) 100%);
  }
  .series-title {
    position: absolute;
    left: 0;
    top: 0;
    width: 1200px;
    height: 700px;
  }
  .series-title text {
    font-family: "Anton", "Oswald", sans-serif;
    font-size: 820px;
  }
  .series-subtitle {
    position: absolute;
    left: 0;
    right: 0;
    top: 650px;
    margin: 0;
    text-align: center;
    font-family: "Montserrat", "Helvetica Neue", Arial, sans-serif;
    font-weight: 800;
    font-size: 25px;
    letter-spacing: 1.6px;
    line-height: 1;
    text-transform: uppercase;
  }
  .subtitle-question { color: var(--flag-blue); }
  .subtitle-divider { color: var(--divider); font-weight: 400; padding: 0 8px; }
  .subtitle-answer { color: var(--flag-red); }
</style>
</head>
<body>
  <main class="series-graphic">
    <svg class="series-title" viewBox="0 0 1200 700" role="img"
         aria-label="Title 45, the numerals filled with a photograph of the amber lodge residence, tinted blue and red">
      <defs>
        <linearGradient id="digit-four-fill" gradientUnits="userSpaceOnUse" x1="0" y1="15" x2="0" y2="590">
          <stop offset="0" stop-color="#0b4c9c"/>
          <stop offset="0.36" stop-color="#1d5ca8"/>
          <stop offset="0.44" stop-color="#c9d4e2"/>
          <stop offset="0.62" stop-color="#e9edf2"/>
          <stop offset="0.82" stop-color="#6f8aa6"/>
          <stop offset="0.9" stop-color="#24452c"/>
          <stop offset="1" stop-color="#3f6d3a"/>
        </linearGradient>
        <linearGradient id="digit-five-fill" gradientUnits="userSpaceOnUse" x1="0" y1="15" x2="0" y2="590">
          <stop offset="0" stop-color="#9c1a22"/>
          <stop offset="0.36" stop-color="#c8252c"/>
          <stop offset="0.44" stop-color="#f2c8c8"/>
          <stop offset="0.62" stop-color="#f6dede"/>
          <stop offset="0.82" stop-color="#c8646a"/>
          <stop offset="0.9" stop-color="#5e1518"/>
          <stop offset="1" stop-color="#8e2426"/>
        </linearGradient>
      </defs>
      <text class="title-digit title-digit--four" x="381" y="590"
            textLength="228" lengthAdjust="spacingAndGlyphs"
            fill="url(#digit-four-fill)">4</text>
      <text class="title-digit title-digit--five" x="598" y="590"
            textLength="221" lengthAdjust="spacingAndGlyphs"
            fill="url(#digit-five-fill)">5</text>
    </svg>
    <p class="series-subtitle">
      <span class="subtitle-question">Who will it be</span><span class="subtitle-divider">|</span><span class="subtitle-answer">Does it matter</span>
    </p>
  </main>
</body>
</html>
```